Bref créative
Business Cards, Letterhead, Envelope
One sided bus card - business letterhead
Professional
Marc D. Venholt
Owner
418 Varnell Ct.
Folsom, CA 95742
marc.venholt@brisktallypartners.example
www.brisktallypartners.example
NOTE: The name of my company is Brisk Tally Partners. Please include that on the cards, letterhead and envelope.
Also, I need to be sure the business card file I get back is editable so that I can make cards for others in my company. I also want to be sure the letterhead file is one that can be pasted into a word document and that I can type over it so that the Word file appears to have letterhead and prints with letterhead.

```html
<!DOCTYPE html>
<html lang="en">
<head>
<meta charset="utf-8">
<title>Brisk Tally Partners – Business Card</title>
<link href="https://fonts.googleapis.com/css2?family=Arimo:wght@400;700&family=Tinos:wght@700&display=swap" rel="stylesheet">
<style>
  :root {
    --page-bg: #e9e9ea;
    --card-bg: #ffffff;
    --ink: #1a1a1a;
    --ink-soft: #3a3a3a;
    --navy: #123a66;
    --blue: #1b6fa8;
    --cyan: #37a6d9;
    --green: #5a9a2c;
    --card-shadow: rgba(0,0,0,0.18);
  }
  * { margin: 0; padding: 0; box-sizing: border-box; }
  html, body {
    width: 1200px; height: 1023px; overflow: hidden;
    background: var(--page-bg);
    font-family: "Arimo", Arial, sans-serif;
    color: var(--ink);
  }
  .canvas { position: relative; width: 1200px; height: 1023px; }
  .card {
    position: absolute;
    background: var(--card-bg);
    border-radius: 16px;
    overflow: hidden;
    box-shadow: 0 6px 18px var(--card-shadow);
  }
  .card--front { left: 125px; top: 111px; width: 610px; height: 346px; }
  .card--back  { left: 435px; top: 493px; width: 604px; height: 344px; }

  .wordmark {
    position: absolute;
    display: flex; align-items: center; gap: 12px;
    font-family: "Arimo", Arial, sans-serif;
    font-weight: 700;
    color: var(--navy);
    letter-spacing: 1px;
    line-height: 1;
  }
  .wordmark__square { background: var(--navy); }
  .card--front .wordmark { left: 40px; top: 210px; font-size: 52px; }
  .card--front .wordmark__square { width: 24px; height: 24px; }

  .contact { position: absolute; left: 290px; top: 76px; }
  .contact__name { font-size: 18px; font-weight: 700; line-height: 22px; }
  .contact__title { font-size: 12px; color: var(--ink-soft); line-height: 16px; }
  .contact__address { font-size: 11px; line-height: 15px; margin-top: 52px; }
  .contact__phones { font-size: 11px; line-height: 14px; margin-top: 12px; }
  .contact__phones b { display: inline-block; width: 12px; }
  .contact__web { font-size: 11px; line-height: 14px; margin-top: 18px; }
  .contact__web .url { font-weight: 700; }

  .band { position: absolute; left: 0; right: 0; bottom: 0; height: 36px; }
  .band__main {
    position: absolute; left: 0; right: 0; top: 0; height: 24px;
    background: linear-gradient(90deg, var(--navy) 0%, var(--blue) 40%, var(--cyan) 68%, var(--green) 100%);
  }
  .band__under {
    position: absolute; left: 0; right: 0; bottom: 0; height: 12px;
    background: linear-gradient(90deg, var(--cyan) 0%, var(--blue) 60%, var(--green) 100%);
  }
  .band__name {
    position: absolute; left: 70px; top: 3px;
    font-family: "Tinos", "Times New Roman", serif;
    font-weight: 700; font-size: 17px; line-height: 18px; color: #ffffff;
  }

  .card--back .wordmark { left: 0; right: 0; top: 190px; justify-content: center; font-size: 60px; }
  .card--back .wordmark__square { width: 28px; height: 28px; }
  .back__company {
    position: absolute; left: 0; right: 0; top: 306px; text-align: center;
    font-family: "Tinos", "Times New Roman", serif;
    font-weight: 700; font-size: 20px; line-height: 22px; color: var(--ink);
  }
</style>
</head>
<body>
<main class="canvas">
  <section class="card card--front" aria-label="Business card front">
    <div class="wordmark"><span class="wordmark__square"></span><span>BTP</span></div>
    <div class="contact">
      <p class="contact__name">Marc D. Venholt</p>
      <p class="contact__title">Owner</p>
      <p class="contact__address">418 Varnell Ct.<br>Larkmoor, OR 95742</p>
      <p class="contact__phones">
        <b>P</b>: 707-555-0142<br>
        <b>C</b>: 707-555-0178<br>
        <b>F</b>: 707-555-0193
      </p>
      <p class="contact__web">
        <b>E</b> : marc.venholt@brisktallypartners.example<br>
        <span class="url">www.brisktallypartners.example</span>
      </p>
    </div>
    <div class="band">
      <div class="band__main"></div>
      <div class="band__under"></div>
      <span class="band__name">Brisk Tally Partners</span>
    </div>
  </section>

  <section class="card card--back" aria-label="Business card back">
    <div class="wordmark"><span class="wordmark__square"></span><span>BTP</span></div>
    <p class="back__company">Brisk Tally Partners</p>
  </section>
</main>
</body>
</html>
```